Design iOS App UI/UX for HouseVerdict.com

Design UI for home screen/dashboard for my iOS/Android APP HouseVerdict.
See attached screen shots and User Experience description. Also go to www.HouseVerdict.com and see the website description (yes, it is still under construction, its broken and incomplete).
You are designing screen #2 #5 #6A, #6B 2&5 are very similar and 6A&6B are very similar.
To understand what you are working on, the main 8 functions of the App are:
Screen: Description:
5, 6D, 6D Get Property Info
6A, 6B, 7 Get After Repaired Value
9, 10, 11 Build a Budget
14, 14A, 15 Calculate Cost of Money
18, 19 Estimate Closing Costs
13, 13B 13A Enter Holding Costs
16, 17 Predict Cost of Sale
1, 2 Let the Dashboard drive your decision
The design aesthetic we are seeking is like the Brackhome.com App, and the Nesvra App.
-Open your iOS 7 mail and launch the "new message" icon and the email template is similar to what we are looking for in UI design:
-Open your iOS 7 calendar and see transitions as you click from day to week to month for the kind of UX design input we are seeking
-We don't want special coding, but off the shelf solutions. So we want you to know what can be built with available code.
Thanks,
Walt Brennick
P.S. Please send description of your experience and links to your work.
Target Market(s)
Our Target User #1 is a house remodel guy, 50 yrs old, skilled blue collar with some college and hands on attitude.
Our Target User #2 is a Realtor who sells these houses for the remodel Fix and Flip guy.
Our Target User #3 is a Hard Money Lender who lends money to our Fix and Flip guy. He is a small business loaning 100k to 300k to our flip guys for each project. He is lending his money, or money he has personally guaranteed with local banks or friends and family.
Our Target User #4 is a landlord looking to evaluate a buy and fix and hold property. Very similar to the User #1, but he spends time managing rental property.
Industry/Entity Type
Construction
Requirements
Must have
- Easy to see, read, clean design.
The top of screen #2 should show the Profit more clearly and compare it to the "70% ARV" scenario.
the 3,6 9 months can be buttons or shown smaller somehow.
Nice to have
- Flat design. clean and lean. look at the work of Lars Ormund if you want to get creative.
Should not have
- flashy splashy, music label like, fashion model like, hokey, cute, silly, kitchy, country, 3-D.

```html
<!DOCTYPE html>
<html lang="en">
<head>
<meta charset="utf-8">
<title>HouseVerdict – Property Detail</title>
<link rel="stylesheet" href="https://fonts.googleapis.com/css2?family=Roboto:wght@300;400&display=swap">
<style>
  :root {
    --page-bg: #e9ebee;
    --screen-bg: #f4f5f7;
    --card-bg: #ffffff;
    --ink: #333333;
    --ink-soft: #9a9a9a;
    --rule: #6b6b6b;
    --accent: #4aaee3;
    --accent-pale: #abcde0;
    --navy: #1f4f82;
    --chip-off: #e3e3e3;
    --chip-off-ink: #c2c2c2;
    --ribbon: #a51c1f;
    --photo-sky: #3f72c6;
    --photo-lawn: #5d8a2f;
  }
  * { box-sizing: border-box; margin: 0; padding: 0; }
  html, body { width: 1200px; height: 1000px; overflow: hidden; }
  body {
    background: var(--page-bg);
    font-family: "Roboto", "Helvetica Neue", Arial, sans-serif;
    font-weight: 300;
    color: var(--ink);
    position: relative;
  }
  .screen {
    position: absolute;
    left: 330px; top: 20px;
    width: 540px; height: 960px;
    background: var(--screen-bg);
    overflow: hidden;
    box-shadow: 0 2px 14px rgba(0,0,0,.12);
  }
  .abs { position: absolute; }
  .status-bar { left: 0; top: 8px; width: 100%; height: 26px; font-size: 18px; font-weight: 400; }
  .status-bar .signal { left: 16px; top: 7px; }
  .status-bar .time { left: 0; width: 100%; text-align: center; top: 2px; }
  .status-bar .battery { right: 20px; top: 5px; }

  .nav-title { left: 0; width: 100%; top: 68px; text-align: center; font-size: 33px; }
  .nav-back { left: 30px; top: 70px; }
  .nav-share { right: 24px; top: 64px; }
  .nav-rule { left: 13px; right: 14px; top: 119px; height: 1px; background: var(--rule); }

  .photo-card { left: 5px; top: 138px; width: 530px; height: 357px; background: var(--card-bg);
    box-shadow: 0 1px 4px rgba(0,0,0,.12); }
  .photo { left: 10px; top: 12px; width: 509px; height: 340px;
    background: linear-gradient(180deg, var(--photo-sky) 0%, #8aa7c9 35%, #a08a6e 55%, var(--photo-lawn) 85%, #4c7526 100%); }
  .ribbon { left: 10px; top: 37px; }
  .ribbon-text { left: 16px; top: 42px; color: #fff; font-size: 20px; font-weight: 400; }
  .pager { right: 30px; top: 505px; font-size: 15px; font-weight: 400; }

  .month-switcher { left: 0; width: 100%; top: 520px; display: flex; justify-content: center; gap: 13px; }
  .month { width: 60px; height: 60px; border-radius: 50%; display: flex; align-items: center; justify-content: center;
    font-size: 38px; background: var(--chip-off); color: var(--chip-off-ink); }
  .month.is-active { background: var(--accent); color: #2a5d80; }
  .month-label { left: 0; width: 100%; top: 581px; text-align: center; font-size: 20px; font-weight: 400; }

  .stats-card { left: 18px; top: 607px; width: 502px; height: 269px; background: var(--card-bg);
    box-shadow: 0 1px 4px rgba(0,0,0,.1); }
  .chart { left: 0; top: 0; }
  .pct { font-size: 34px; color: var(--navy); }
  .pct-arv { left: 230px; top: 17px; }
  .pct-arv-label { left: 274px; top: 60px; font-size: 13px; color: var(--ink-soft); font-weight: 400; }
  .pct-profit { left: 230px; top: 130px; }
  .profit-value { left: 42px; top: 190px; font-size: 28px; }
  .profit-label { left: 140px; top: 222px; font-size: 20px; color: var(--ink-soft); }
  .col-rule { left: 354px; top: 20px; width: 1px; height: 230px; background: #d6d6d6; }
  .spec { left: 388px; width: 90px; text-align: left; }
  .spec .count { position: absolute; left: 0; top: 8px; font-size: 26px; }
  .spec .name { position: absolute; left: 0; width: 80px; top: 42px; text-align: center; font-size: 16px; font-weight: 400; }
  .spec svg { position: absolute; left: 28px; top: 2px; }
  .spec-beds { top: 18px; }
  .spec-baths { top: 106px; }
  .spec-garage { top: 190px; }
  .more { left: 487px; top: 116px; }

  .target-label { left: 34px; top: 890px; font-size: 26px; color: #b0b0b0; }
  .target-value { right: 28px; top: 889px; font-size: 30px; font-weight: 400; }
</style>
</head>
<body>
<main class="screen">
  <div class="status-bar abs">
    <svg class="signal abs" width="58" height="12" viewBox="0 0 58 12" aria-hidden="true">
      <circle cx="6" cy="6" r="5" fill="#333"/><circle cx="17" cy="6" r="5" fill="#333"/><circle cx="28" cy="6" r="5" fill="#333"/>
      <circle cx="39" cy="6" r="4.5" fill="none" stroke="#333"/><circle cx="50" cy="6" r="4.5" fill="none" stroke="#333"/>
    </svg>
    <span class="time abs">4:21 PM</span>
    <svg class="battery abs" width="40" height="18" viewBox="0 0 40 18" aria-hidden="true">
      <rect x="1" y="1" width="34" height="16" rx="3" fill="none" stroke="#333" stroke-width="1.5"/>
      <rect x="4" y="4" width="9" height="10" fill="#333"/><rect x="36" y="6" width="3" height="6" fill="#333"/>
    </svg>
  </div>

  <svg class="nav-back abs" width="22" height="36" viewBox="0 0 22 36" aria-label="Back">
    <polyline points="19,2 3,18 19,34" fill="none" stroke="#333" stroke-width="2.5"/>
  </svg>
  <h1 class="nav-title abs" style="font-weight:300">418 Marlow DR</h1>
  <svg class="nav-share abs" width="34" height="44" viewBox="0 0 34 44" aria-label="Share">
    <path d="M11 14 H2 V42 H32 V14 H23" fill="none" stroke="#333" stroke-width="2"/>
    <line x1="17" y1="2" x2="17" y2="28" stroke="#333" stroke-width="2"/>
    <polyline points="9,10 17,2 25,10" fill="none" stroke="#333" stroke-width="2"/>
  </svg>
  <div class="nav-rule abs"></div>

  <section class="photo-card abs">
    <div class="photo abs" role="img" aria-label="Photo of the property: two-storey stone house with gabled roof, arched windows, trees and front lawn"></div>
    <svg class="ribbon abs" width="132" height="40" viewBox="0 0 132 40" aria-hidden="true">
      <polygon points="0,0 132,0 120,20 132,40 0,40" fill="var(--ribbon)"/>
    </svg>
    <span class="ribbon-text abs">14% Profit</span>
  </section>
  <span class="pager abs">1 of 25</span>

  <nav class="month-switcher abs" aria-label="Holding period">
    <span class="month is-active">3</span>
    <span class="month">6</span>
    <span class="month">9</span>
  </nav>
  <span class="month-label abs">Months</span>

  <section class="stats-card abs">
    <svg class="chart abs" width="340" height="269" viewBox="0 0 340 269" aria-label="Pie chart: profit 26% compared with 70% ARV">
      <path d="M109,107 L145.5,170.2 A73,73 0 1,0 72.5,170.2 Z" fill="var(--accent-pale)"/>
      <path d="M112,100 L127,158 A48,48 0 0,1 85,162 Z" fill="var(--accent)"/>
      <path d="M112,100 L127,158 L132,154 Z" fill="var(--navy)"/>
      <line x1="95" y1="87" x2="305" y2="87" stroke="var(--navy)" stroke-width="1.2"/>
      <line x1="132" y1="166" x2="305" y2="166" stroke="var(--navy)" stroke-width="1.2"/>
    </svg>
    <span class="pct pct-arv abs">70%</span>
    <span class="pct-arv-label abs">ARV</span>
    <span class="pct pct-profit abs">26%</span>
    <span class="profit-value abs">$34,994</span>
    <span class="profit-label abs">Profit</span>

    <div class="col-rule abs"></div>

    <div class="spec spec-beds abs">
      <span class="count">4</span>
      <svg width="44" height="30" viewBox="0 0 44 30" aria-hidden="true">
        <rect x="2" y="4" width="4" height="24" fill="#222"/><rect x="2" y="16" width="40" height="7" fill="#222"/>
        <rect x="38" y="16" width="4" height="12" fill="#222"/><rect x="9" y="9" width="12" height="6" rx="3" fill="#222"/>
        <rect x="22" y="11" width="20" height="4" fill="#222"/>
      </svg>
      <span class="name">Beds</span>
    </div>
    <div class="spec spec-baths abs">
      <span class="count">2</span>
      <svg width="44" height="34" viewBox="0 0 44 34" aria-hidden="true">
        <circle cx="11" cy="4" r="3.5" fill="#222"/><rect x="6" y="9" width="10" height="13" fill="#222"/>
        <rect x="6.5" y="22" width="3.5" height="11" fill="#222"/><rect x="12" y="22" width="3.5" height="11" fill="#222"/>
        <line x1="22" y1="0" x2="22" y2="34" stroke="#222" stroke-width="1.5"/>
        <circle cx="33" cy="4" r="3.5" fill="#222"/><polygon points="33,8 41,24 25,24" fill="#222"/>
        <rect x="28.5" y="24" width="3.5" height="9" fill="#222"/><rect x="34" y="24" width="3.5" height="9" fill="#222"/>
      </svg>
      <span class="name">Baths</span>
    </div>
    <div class="spec spec-garage abs">
      <span class="count">1</span>
      <svg width="50" height="28" viewBox="0 0 50 28" aria-hidden="true">
        <path d="M4 14 L12 4 H34 L42 13 H47 V21 H3 V14 Z" fill="#222"/>
        <rect x="15" y="7" width="8" height="6" fill="#fff"/><rect x="25" y="7" width="8" height="6" fill="#fff"/>
        <circle cx="13" cy="22" r="5" fill="#222" stroke="#fff" stroke-width="1.5"/>
        <circle cx="37" cy="22" r="5" fill="#222" stroke="#fff" stroke-width="1.5"/>
      </svg>
      <span class="name">Garage</span>
    </div>

    <svg class="more abs" width="30" height="30" viewBox="0 0 30 30" aria-label="More details">
      <circle cx="15" cy="15" r="14" fill="#fff" stroke="#e2e2e2"/>
      <polyline points="12,9 18,15 12,21" fill="none" stroke="#333" stroke-width="1.6"/>
    </svg>
  </section>

  <span class="target-label abs">Target purchase</span>
  <span class="target-value abs">$110,000</span>
</main>
</body>
</html>
```